Classical Chamber Choir needs an electronic and printable flyer for an Easter Concert

I am the new Artistic Director of the Varlow Singers. We would like to advertise our upcoming concert on April 5 and are seeking a new, more youthful, contemporary look for the choir's advertising. Previously they have used classical curly letters and dark colours. Perhaps black/grey and white would work?
The choir is 27 years old and has many loyal and some quite elderly singers. We would now like to extend our appeal to the younger singers who are in the choir - age group 35 - 60 and we are keen to attract more in the 30/40 age group. I would like something contemporary in feel, uncluttered, minimalist and artistically appealing. More Wolanitz than Durac - more Lorvasini than Halvick. Some inspiration starters: Tedrilo line drawings, linocut designs, Ivor Hadcombe pencil drawings. I am hoping these references might inspire you. Here are some other ideas using line from Dénes Halkó:
https://photos.web.vlx.io/mT4pLwRyh82BnWcaQ
https://photos.web.vlx.io/3HRnVkTaWpDcuLe48
We would require an A4 flyer, (high res. and low res.) DL, jpg for Gridwave and a 10cm. size to put on the front of the Concert Programme.

```html
<!DOCTYPE html>
<html lang="en">
<head>
<meta charset="utf-8">
<title>Varlow Singers – Halbreck at Easter flyer variants</title>
<link rel="stylesheet" href="https://fonts.googleapis.com/css2?family=Bebas+Neue&family=Jost:wght@300;400&display=swap">
<style>
  :root {
    --page: #ffffff;
    --blue-bg: #18a9dc;
    --blue-box: #0a85bc;
    --blue-accent: #e3fb2c;
    --blue-ink: #0e2233;
    --tan-bg: #b0926e;
    --tan-box: #957d5c;
    --tan-accent: #2a2118;
    --tan-ink: #2a2118;
    --light: #ffffff;
  }
  * { box-sizing: border-box; margin: 0; padding: 0; }
  html, body { width: 1200px; height: 890px; overflow: hidden; background: var(--page); }
  body { position: relative; font-family: "Jost", sans-serif; font-weight: 300; color: var(--light); }

  .flyer {
    position: absolute; top: 54px; width: 518px; height: 776px; overflow: hidden;
    background: var(--bg);
  }
  .flyer--blue { left: 55px; --bg: var(--blue-bg); --box: var(--blue-box); --accent: var(--blue-accent); --ink: var(--blue-ink); --title: var(--blue-accent); }
  .flyer--tan  { left: 622px; --bg: var(--tan-bg); --box: var(--tan-box); --accent: var(--tan-accent); --ink: var(--tan-ink); --title: var(--light); }

  .art { position: absolute; }
  .art--music { left: 16px; top: 66px; width: 440px; height: 200px; border-radius: 50% 40% 45% 50%;
    background: radial-gradient(ellipse at 30% 40%, rgba(255,255,255,.32), rgba(255,255,255,0) 70%); }
  .art--willow { left: 409px; top: 42px; width: 108px; height: 236px;
    background: linear-gradient(200deg, rgba(20,20,20,.18), rgba(20,20,20,.05)); border-radius: 40% 40% 20% 20%; }
  .art--violin { left: 0; top: 248px; width: 181px; height: 478px;
    background: linear-gradient(180deg, rgba(20,20,20,.06), rgba(20,20,20,.18)); border-radius: 30% 45% 45% 30% / 20% 40% 40% 20%; }

  .presenter { position: absolute; left: 53px; top: 51px; font-size: 18px; font-weight: 300;
    letter-spacing: 9.6px; white-space: nowrap; }
  .headline { position: absolute; left: 127px; top: 92px; font-family: "Bebas Neue", sans-serif;
    font-size: 82px; line-height: 1; color: var(--title); letter-spacing: 0; white-space: nowrap; }
  .subhead { position: absolute; left: 161px; top: 160px; font-size: 40px; font-weight: 300;
    letter-spacing: 0.5px; color: var(--ink); line-height: 1; white-space: nowrap; }

  .programme { position: absolute; left: 162px; top: 265px; font-size: 17px; line-height: 19.8px; white-space: nowrap; }

  .rule { position: absolute; left: 162px; width: 301px; height: 1px; background: rgba(255,255,255,.75); }
  .rule--top { top: 362px; }
  .rule--bottom { top: 452px; }

  .venue { position: absolute; left: 162px; top: 372px; white-space: nowrap; }
  .venue__name { font-size: 22.5px; font-weight: 300; color: var(--accent); line-height: 26px; }
  .venue__street { font-size: 11.5px; line-height: 16px; }
  .venue__date { font-size: 22px; line-height: 26px; margin-top: 2px; }

  .credits { position: absolute; top: 472px; font-size: 12.5px; line-height: 14.6px; white-space: nowrap; }
  .credits--left { left: 219px; }
  .credits--right { left: 362px; }
  .credits h3 { font-weight: 300; font-size: 12.5px; color: var(--ink); }
  .credits p { font-weight: 300; }
  .credits .gap { margin-top: 14.6px; }

  .tickets { position: absolute; left: 259px; top: 638px; width: 208px; height: 84px;
    border-radius: 7px; background: var(--box); padding: 13px 19px; white-space: nowrap; }
  .tickets__label { font-size: 15px; line-height: 18px; color: var(--accent); }
  .tickets__price { font-size: 16.5px; line-height: 20px; font-weight: 300; }
  .tickets__note { font-size: 12px; line-height: 16px; }

  .note { position: absolute; left: 265px; top: 726px; font-size: 12.5px; white-space: nowrap; }
</style>
</head>
<body>

<section class="flyer flyer--blue" aria-label="Concert flyer, blue version">
  <div class="art art--music" role="img" aria-label="Pale treble clef and flowing music staff with notes"></div>
  <div class="art art--willow" role="img" aria-label="Line drawing of a tied bunch of pussy willow branches"></div>
  <div class="art art--violin" role="img" aria-label="Sketched line drawing of a violin"></div>

  <p class="presenter">VARLOW SINGERS PRESENT</p>
  <h1 class="headline">HALBRECK</h1>
  <h2 class="subhead">AT EASTER</h2>

  <p class="programme">HALBRECK STABAT MATER D 383<br>in the company of the<br>RUSSIAN MASTERS<br>Chervakov, Glenkov, Ravelinsky, Borovets</p>

  <div class="rule rule--top"></div>
  <div class="venue">
    <p class="venue__name">ST AUBERT CLEMENT CHURCH</p>
    <p class="venue__street">MARLOW STREET FERNWOOD HILL</p>
    <p class="venue__date">5PM APRIL 5 2020</p>
  </div>
  <div class="rule rule--bottom"></div>

  <div class="credits credits--left">
    <h3>SOLOISTS</h3>
    <p>Lena Varsholt<br>Adrian Colvey<br>Gerald Farnum</p>
    <h3 class="gap">MEN OF TONE</h3>
    <h3 class="gap">ARTISTIC DIRECTOR</h3>
    <p>Erika Moldvary</p>
  </div>
  <div class="credits credits--right">
    <h3>STRING QUARTET</h3>
    <p>Emil Sorvatin<br>Maya Pellan<br>Roland Hesket<br>Zsolt Tarnai</p>
    <h3 class="gap">ORGAN</h3>
    <p>Josette Arlen</p>
  </div>

  <div class="tickets">
    <p class="tickets__label">TICKETS</p>
    <p class="tickets__price">$30/ $25/ $10 Student</p>
    <p class="tickets__note">Children under 12 free</p>
  </div>
  <p class="note">Programmes: Gold Coin Donation</p>
</section>

<section class="flyer flyer--tan" aria-label="Concert flyer, tan version">
  <div class="art art--music" role="img" aria-label="Pale treble clef and flowing music staff with notes"></div>
  <div class="art art--willow" role="img" aria-label="Line drawing of a tied bunch of pussy willow branches"></div>
  <div class="art art--violin" role="img" aria-label="Sketched line drawing of a violin"></div>

  <p class="presenter">VARLOW SINGERS PRESENT</p>
  <h1 class="headline">HALBRECK</h1>
  <h2 class="subhead">AT EASTER</h2>

  <p class="programme">HALBRECK STABAT MATER D 383<br>in the company of the<br>RUSSIAN MASTERS<br>Chervakov, Glenkov, Ravelinsky, Borovets</p>

  <div class="rule rule--top"></div>
  <div class="venue">
    <p class="venue__name">ST AUBERT CLEMENT CHURCH</p>
    <p class="venue__street">MARLOW STREET FERNWOOD HILL</p>
    <p class="venue__date">5PM APRIL 5 2020</p>
  </div>
  <div class="rule rule--bottom"></div>

  <div class="credits credits--left">
    <h3>SOLOISTS</h3>
    <p>Lena Varsholt<br>Adrian Colvey<br>Gerald Farnum</p>
    <h3 class="gap">MEN OF TONE</h3>
    <h3 class="gap">ARTISTIC DIRECTOR</h3>
    <p>Erika Moldvary</p>
  </div>
  <div class="credits credits--right">
    <h3>STRING QUARTET</h3>
    <p>Emil Sorvatin<br>Maya Pellan<br>Roland Hesket<br>Zsolt Tarnai</p>
    <h3 class="gap">ORGAN</h3>
    <p>Josette Arlen</p>
  </div>

  <div class="tickets">
    <p class="tickets__label">TICKETS</p>
    <p class="tickets__price">$30/ $25/ $10 Student</p>
    <p class="tickets__note">Children under 12 free</p>
  </div>
  <p class="note">Programmes: Gold Coin Donation</p>
</section>

</body>
</html>
```